Used Semi Truck Website Redesign

We are redoing the website backend and would like to also do a front end redesign. I would like a Mobile and Desktop mockup for each page. The website has more mobile visitors than desktop visitors. Our competitor is http://www.haulmarketbay.example. We don't want to copy them exactly but we want a site that looks more like that. We need the functionality of that site. One big difference is that we also sell parts and trailers.

We need a redesign for front page, product detail page, search result page, content page. It is very important that the site is very easy to use on mobile devices. Our target audience is Truck drivers.

Feel free to use demo fonts stock images, and icons. We will purchase necessary 3rd party media when a winner is chosen.

Target Market(s)

People who want to buy used trucks.

Coding

Coded - Design and coding required

Number of Pages Required

5+ page

Requirements
Must have
• Mockup for Desktop and Mobile pages.

```html
<!DOCTYPE html>
<html lang="en">
<head>
<meta charset="utf-8">
<title>RHX Trucks – Used Trucks, Trailers and Parts</title>
<link href="https://fonts.googleapis.com/css2?family=Lato:wght@400;700&family=Open+Sans:wght@400;600;700&family=Roboto+Slab:wght@700&display=swap" rel="stylesheet">
<style>
:root{
  --red:#e31e24;
  --red-dark:#b3141a;
  --orange:#f9a11b;
  --orange-deep:#f07f12;
  --charcoal:#2e2e2e;
  --ink:#222;
  --muted:#8a8a8a;
  --line:#dcdcdc;
  --topbar:#eeeeee;
  --band:#eceef1;
  --sky:#1ca4dd;
  --link-blue:#29a9e0;
  --footer:#3b3b3b;
  --footer-base:#2c2c2c;
  --footer-text:#c9c9c9;
  --white:#fff;
}
*{box-sizing:border-box;margin:0;padding:0}
html,body{width:1200px;height:2525px;overflow:hidden}
body{position:relative;background:var(--white);font-family:"Lato",sans-serif;color:var(--ink)}
.abs{position:absolute}
ul{list-style:none}

/* top bar */
.topbar{left:0;top:0;width:1200px;height:34px;background:var(--topbar)}
.topbar .social{left:146px;top:9px;display:flex;gap:14px}
.topbar .social span{width:15px;height:15px;border-radius:50%;background:#b5b5b5;display:block}
.topbar .utility{right:135px;top:0;display:flex;height:34px}
.topbar .utility a{font-family:"Open Sans",sans-serif;font-size:14px;color:#333;text-decoration:none;padding:0 14px;line-height:34px;border-left:1px solid #d4d4d4}
.topbar .utility a:first-child{border-left:none}

/* header */
.header{left:0;top:34px;width:1200px;height:104px;background:var(--white)}
.brand{left:131px;top:30px;font-family:"Roboto Slab",serif;font-weight:700;font-size:36px;color:var(--red);letter-spacing:.5px}
.header-btn{top:40px;width:118px;height:37px;border:2px solid;font-family:"Open Sans",sans-serif;font-size:17px;font-weight:600;display:flex;align-items:center;justify-content:center}
.btn-find{left:793px;border-color:var(--red);color:var(--red)}
.btn-sell{left:917px;border-color:var(--orange);color:var(--orange)}

/* hero */
.hero{left:0;top:138px;width:1200px;height:470px;overflow:hidden}
.hero-photo{position:absolute;inset:0;background:linear-gradient(180deg,#4b4d55 0%,#6e5d58 30%,#8b6a5a 45%,#4a4744 70%,#2d2c2d 100%)}
.hero-title{position:absolute;left:0;width:1200px;text-align:center;color:var(--white);font-family:"Open Sans",sans-serif;text-shadow:0 1px 3px rgba(0,0,0,.4)}
.hero-title .l1{display:block;position:absolute;top:88px;width:100%;font-size:30px;font-weight:600}
.hero-title .l2{display:block;position:absolute;top:115px;width:100%;font-size:45px;font-weight:700}
.quick-search{left:224px;top:204px;width:757px;height:168px;background:var(--red);box-shadow:0 4px 14px rgba(0,0,0,.35)}
.quick-search h2{position:absolute;left:37px;top:14px;color:var(--white);font-family:"Open Sans",sans-serif;font-weight:600;font-size:21px}
.field{position:absolute;height:38px;background:var(--white);border:1px solid #ddd;font-family:"Open Sans",sans-serif;font-size:12px;color:#9a9a9a;padding-left:15px;display:flex;align-items:center}
.field.select::after{content:"";position:absolute;right:14px;top:12px;width:8px;height:8px;border-right:1.5px solid #888;border-bottom:1.5px solid #888;transform:rotate(45deg)}
.search-btn{position:absolute;left:505px;top:101px;width:225px;height:40px;background:var(--orange);color:var(--white);font-family:"Open Sans",sans-serif;font-weight:600;font-size:17px;display:flex;align-items:center;justify-content:center}
.dots{left:568px;top:440px;display:flex;gap:8px}
.dots span{width:13px;height:13px;border-radius:50%;background:var(--white)}
.dots span:first-child{background:transparent;border:2px solid var(--white)}

/* category cards */
.cat-card{top:631px;width:308px;height:340px;border:1px solid var(--line);background:var(--white);overflow:hidden}
.cat-top{position:absolute;left:0;top:0;width:308px;height:132px}
.cat-top svg.wave{position:absolute;left:0;top:0}
.cat-icon{position:absolute;left:50%;top:22px;transform:translateX(-50%)}
.cat-card h3{position:absolute;left:0;top:139px;width:100%;text-align:center;font-family:"Open Sans",sans-serif;font-weight:600;font-size:19px;color:var(--ink)}
.cat-card .sub{position:absolute;left:0;top:168px;width:100%;text-align:center;font-size:12.5px;color:var(--muted)}
.cat-list{position:absolute;left:32px;top:206px;width:270px;display:grid;grid-template-columns:158px 1fr;row-gap:7px}
.cat-list li{font-size:12px;color:#555;position:relative;padding-left:11px}
.cat-list li::before{content:"";position:absolute;left:0;top:4px;width:4px;height:4px;border-right:1.5px solid var(--red);border-bottom:1.5px solid var(--red);transform:rotate(-45deg)}
.view-all{position:absolute;left:79px;top:289px;width:138px;height:37px;border:2px solid var(--orange);color:var(--orange);font-size:13px;display:flex;align-items:center;justify-content:center}

/* featured ads */
.section-title{font-family:"Lato",sans-serif;font-size:27px;color:var(--ink)}
.featured-title{left:130px;top:1008px}
.arrow-btn{top:1016px;width:21px;height:21px;border-radius:50%;background:#e2e2e2}
.arrow-btn::after{content:"";position:absolute;top:7px;width:6px;height:6px;border-left:1.5px solid #666;border-bottom:1.5px solid #666}
.arrow-prev{left:1025px}.arrow-prev::after{left:8px;transform:rotate(45deg)}
.arrow-next{left:1052px}.arrow-next::after{left:6px;transform:rotate(-135deg)}
.ad-card{top:1060px;width:230px;height:246px;border:1px solid var(--line);background:var(--white)}
.ad-photo{width:100%;height:143px}
.ad-card h4{margin-top:15px;text-align:center;font-family:"Open Sans",sans-serif;font-weight:400;font-size:16px;color:var(--red)}
.ad-card p{margin-top:3px;text-align:center;font-size:12px;color:var(--muted)}
.ad-card .price{margin-top:6px;font-family:"Open Sans",sans-serif;font-size:18px;font-weight:700;color:var(--ink)}

/* states */
.state-band{left:0;top:1368px;width:1200px;height:355px;background:linear-gradient(90deg,#eef0f2,#e7e9ec 60%,#eceef0)}
.state-title{left:130px;top:1424px}
.state-cols{left:133px;top:1486px;display:flex}
.state-cols ul li{font-size:12.5px;color:#333;height:26px;line-height:20px}
.state-cols ul:nth-child(1){width:121px}
.state-cols ul:nth-child(2){width:136px}
.state-cols ul:nth-child(3){width:122px}
.state-cols ul:nth-child(4){width:136px}
.dealer-box{left:789px;top:1412px;width:283px;height:252px;background:linear-gradient(180deg,var(--orange) 0%,var(--orange-deep) 45%,var(--red-dark) 100%);color:var(--white);text-align:center}
.dealer-map{position:absolute;left:64px;top:18px;width:155px;height:82px;border-radius:40px;background:rgba(255,255,255,.85)}
.dealer-box h3{position:absolute;top:98px;width:100%;font-family:"Open Sans",sans-serif;font-weight:400;font-size:24px}
.dealer-box p{position:absolute;left:30px;top:133px;width:223px;font-size:12px;line-height:17px;color:#fde7d7}
.dealer-btn{position:absolute;left:88px;top:182px;width:118px;height:30px;border:1px solid var(--white);font-size:12px;display:flex;align-items:center;justify-content:center}

/* blogs */
.panel{top:1760px;width:462px;height:352px;border:1px solid var(--line);background:var(--white)}
.blogs{left:128px}
.blogs h2{position:absolute;left:32px;top:18px;font-weight:400;font-size:25px;color:var(--ink)}
.blog-item{position:absolute;left:32px;width:410px;height:84px}
.blog-thumb{position:absolute;left:0;top:0;width:113px;height:80px}
.blog-item h4{position:absolute;left:132px;top:-2px;font-family:"Open Sans",sans-serif;font-weight:400;font-size:15px;color:var(--ink)}
.blog-item p{position:absolute;left:132px;top:22px;width:270px;font-size:11.5px;line-height:17px;color:var(--muted)}
.blog-item a{position:absolute;left:132px;top:60px;font-size:11.5px;color:var(--red);text-decoration:none;font-weight:700}
.more-blogs{position:absolute;left:32px;top:289px;width:166px;height:34px;background:var(--red);color:var(--white);font-size:12.5px;font-weight:700;display:flex;align-items:center;justify-content:center}

/* feed */
.feed{left:608px}
.feed-head{position:absolute;left:-1px;top:-1px;width:462px;height:48px;background:var(--sky);color:var(--white);font-family:"Open Sans",sans-serif;font-size:23px;padding:10px 0 0 30px}
.follow-chip{position:absolute;right:14px;top:12px;width:52px;height:17px;background:#e6f4fb;border-radius:2px}
.feed-item{position:absolute;left:34px;width:390px}
.avatar{position:absolute;left:0;top:0;width:46px;height:46px;border-radius:50%;background:linear-gradient(135deg,#c7b3a4,#7c6a60)}
.feed-item h4{position:absolute;left:58px;top:0;font-family:"Open Sans",sans-serif;font-weight:400;font-size:14px;color:var(--ink);white-space:nowrap}
.feed-item h4 span{color:var(--muted)}
.feed-item p{position:absolute;left:58px;top:24px;width:340px;font-size:11.5px;line-height:18px;color:var(--muted)}
.feed-item time{position:absolute;left:58px;font-size:11.5px;color:var(--link-blue)}
.scroll-track{position:absolute;right:2px;top:52px;width:9px;height:292px;background:#f2f2f2}
.scroll-thumb{position:absolute;right:2px;top:60px;width:9px;height:102px;background:#c6c6c6}

/* footer */
.footer{left:0;top:2208px;width:1200px;height:258px;background:var(--footer)}
.footer-col{position:absolute;top:54px;height:126px}
.footer-col h5{font-family:"Open Sans",sans-serif;font-weight:700;font-size:15px;color:var(--white);margin-bottom:16px}
.footer-col li{font-size:13.5px;color:var(--footer-text);height:26px}
.footer-col p{font-size:13.5px;color:var(--footer-text)}
.divider{position:absolute;top:54px;width:1px;height:138px;background:#555}
.follow-circles{display:flex;gap:6px;margin-top:16px}
.follow-circles span{width:30px;height:30px;border:1.5px solid var(--white);border-radius:50%}
.footer-base{left:0;top:2466px;width:1200px;height:59px;background:var(--footer-base);text-align:center;font-size:12px;color:#a8a8a8;line-height:59px}
</style>
</head>
<body>

<div class="abs topbar">
  <div class="abs social" aria-label="Social links"><span></span><span></span><span></span><span></span></div>
  <nav class="abs utility"><a>Find a Dealer</a><a>My Trader</a><a>Register</a><a>Login</a></nav>
</div>

<header class="abs header">
  <div class="abs brand">RHX Trucks</div>
  <div class="abs header-btn btn-find">Find</div>
  <div class="abs header-btn btn-sell">Sell</div>
</header>

<section class="abs hero">
  <div class="hero-photo" role="img" aria-label="Photo of a red semi truck hauling a trailer on a highway at sunset"></div>
  <h1 class="hero-title"><span class="l1">WE SELL USED TRUCKS,</span><span class="l2">TRAILERS AND ALSO PARTS</span></h1>
  <form class="abs quick-search">
    <h2>Quick Search</h2>
    <div class="field" style="left:33px;top:54px;width:226px">Type Keyword</div>
    <div class="field select" style="left:269px;top:54px;width:226px">Select Class</div>
    <div class="field select" style="left:505px;top:54px;width:225px">Select Category</div>
    <div class="field select" style="left:33px;top:101px;width:226px">Select a Model</div>
    <div class="field" style="left:269px;top:101px;width:226px">Zip Code</div>
    <div class="search-btn">Search</div>
  </form>
  <div class="abs dots"><span></span><span></span><span></span><span></span></div>
</section>

<!-- categories -->
<article class="abs cat-card" style="left:128px">
  <div class="cat-top">
    <svg class="wave" width="308" height="132"><defs><linearGradient id="gOrange" x1="0" y1="0" x2="0" y2="1"><stop offset="0" stop-color="#fcb900"/><stop offset="1" stop-color="#f58a14"/></linearGradient></defs><path d="M0 0H308V108Q154 150 0 108Z" fill="url(#gOrange)"/></svg>
    <svg class="cat-icon" width="104" height="60" viewBox="0 0 104 60" fill="none" stroke="#fff" stroke-width="4"><rect x="4" y="6" width="62" height="36" rx="3"/><path d="M66 16H86L98 30V42H66Z"/><circle cx="20" cy="48" r="7" fill="#f7a00f"/><circle cx="40" cy="48" r="7" fill="#f7a00f"/><circle cx="84" cy="48" r="7" fill="#f7a00f"/></svg>
  </div>
  <h3>Find Heavy Duty Trucks</h3>
  <div class="sub">What Type Heavy Duty Truck do you need?</div>
  <ul class="cat-list"><li>Cab-Chassis</li><li>Day Cab</li><li>Flatbed-Truck</li><li>Tractor</li><li>Box Truck-Straight Truck</li><li>Crane Truck</li></ul>
  <div class="view-all">VIEW ALL</div>
</article>

<article class="abs cat-card" style="left:449px">
  <div class="cat-top">
    <svg class="wave" width="308" height="132"><defs><linearGradient id="gRed" x1="0" y1="0" x2="0" y2="1"><stop offset="0" stop-color="#f0353a"/><stop offset="1" stop-color="#d9141b"/></linearGradient></defs><path d="M0 0H308V108Q154 150 0 108Z" fill="url(#gRed)"/></svg>
    <svg class="cat-icon" width="90" height="60" viewBox="0 0 90 60" fill="none" stroke="#fff" stroke-width="4"><rect x="4" y="4" width="56" height="40" rx="3"/><path d="M60 16H74L86 30V44H60Z"/><path d="M14 16H50" /><circle cx="22" cy="48" r="7" fill="#e2252b"/><circle cx="70" cy="48" r="7" fill="#e2252b"/></svg>
  </div>
  <h3>Find Medium Duty Trucks</h3>
  <div class="sub">What Type Heavy Duty Truck do you need?</div>
  <ul class="cat-list"><li>Cab-Chassis</li><li>Day Cab</li><li>Flatbed-Truck</li><li>Tractor</li><li>Box Truck-Straight Truck</li><li>Crane Truck</li></ul>
  <div class="view-all">VIEW ALL</div>
</article>

<article class="abs cat-card" style="left:771px">
  <div class="cat-top">
    <svg class="wave" width="308" height="132"><defs><linearGradient id="gDark" x1="0" y1="0" x2="0" y2="1"><stop offset="0" stop-color="#4a4a4a"/><stop offset="1" stop-color="#1e1e1e"/></linearGradient></defs><path d="M0 0H308V108Q154 150 0 108Z" fill="url(#gDark)"/></svg>
    <svg class="cat-icon" width="90" height="60" viewBox="0 0 90 60" style="top:30px"><rect x="8" y="10" width="64" height="20" rx="10" fill="#fff"/><rect x="4" y="30" width="82" height="5" fill="#fff"/><circle cx="56" cy="40" r="5" fill="#fff"/><circle cx="68" cy="40" r="5" fill="#fff"/></svg>
  </div>
  <h3>Find Trailers &amp; Parts</h3>
  <div class="sub">What Type Heavy Duty Truck do you need?</div>
  <ul class="cat-list"><li>Dump Trailer</li><li>Gooseneck Trailer</li><li>Lowboy Trailer</li><li>End Dump Trailer</li><li>Reefer Van</li><li>Utilit Trailer</li></ul>
  <div class="view-all">VIEW ALL</div>
</article>

<!-- featured -->
<h2 class="abs section-title featured-title">Featured Ads</h2>
<div class="abs arrow-btn arrow-prev"></div>
<div class="abs arrow-btn arrow-next"></div>

<article class="abs ad-card" style="left:128px">
  <div class="ad-photo" role="img" aria-label="Photo of a row of white box trucks" style="background:linear-gradient(160deg,#d9dadb,#8e9092)"></div>
  <h4>Truck or Trailer Tittle</h4><p>Mauris vel lacus vitae vestibulum</p><p class="price">$25,150</p>
</article>
<article class="abs ad-card" style="left:367px">
  <div class="ad-photo" role="img" aria-label="Photo of chrome spark plug parts" style="background:linear-gradient(160deg,#eeeeee,#a9a9a9)"></div>
  <h4>Truck or Trailer Tittle</h4><p>Mauris vel lacus vitae vestibulum</p><p class="price">$25,150</p>
</article>
<article class="abs ad-card" style="left:604px">
  <div class="ad-photo" role="img" aria-label="Photo of a dark blue semi truck with a white trailer" style="background:linear-gradient(170deg,#a5b2c4,#2a3348 60%,#55585e)"></div>
  <h4>Truck or Trailer Tittle</h4><p>Mauris vel lacus vitae vestibulum</p><p class="price">$25,150</p>
</article>
<article class="abs ad-card" style="left:842px">
  <div class="ad-photo" role="img" aria-label="Photo of an aluminium utility trailer" style="background:linear-gradient(170deg,#bfc2c4,#e6e7e8 55%,#6d6f71)"></div>
  <h4>Truck or Trailer Tittle</h4><p>Mauris vel lacus vitae vestibulum</p><p class="price">$25,150</p>
</article>

<!-- states -->
<section class="abs state-band" role="img" aria-label="Faded background photo of parked trucks"></section>
<h2 class="abs section-title state-title">Trucks for Sale by State</h2>
<div class="abs state-cols">
  <ul><li>Alabama</li><li>Alaska</li><li>Arizona</li><li>Arkansas</li><li>California</li><li>Colorado</li></ul>
  <ul><li>Connecticut</li><li>Delaware</li><li>Florida</li><li>Georgia</li><li>Hawaii</li><li>Idaho</li></ul>
  <ul><li>Illinois</li><li>Indiana</li><li>Iowa</li><li>Kansas</li><li>Kentucky</li><li>Lousiana</li></ul>
  <ul><li>Maine</li><li>Maryland</li><li>Masachusetts</li><li>Michigan</li><li>Minnesota</li><li>Mississippi</li></ul>
  <ul><li>Missouri</li><li>Montana</li><li>Nebraska</li><li>Nevada</li><li>New Hampshire</li><li>New Jersey</li></ul>
</div>
<aside class="abs dealer-box">
  <div class="dealer-map" role="img" aria-label="White world map illustration"></div>
  <h3>Find a Dealer</h3>
  <p>Mauris vel lacus vitae felis vestibulum volutpat Etiam est nunc venena</p>
  <div class="dealer-btn">CLICK HERE</div>
</aside>

<!-- blogs -->
<section class="abs panel blogs">
  <h2>From Our Blogs</h2>
  <div class="blog-item" style="top:73px">
    <div class="blog-thumb" role="img" aria-label="Photo of a white semi truck" style="background:linear-gradient(160deg,#a9c1dc,#e8eaec 55%,#7a7c80)"></div>
    <h4>Blog Tittle here</h4>
    <p>Mauris vel lacus vitae felis vestibulum volutpat Etiam est nunc venenatis in tristique</p>
    <a>READ MORE</a>
  </div>
  <div class="blog-item" style="top:186px">
    <div class="blog-thumb" role="img" aria-label="Photo of a red semi truck on the road" style="background:linear-gradient(160deg,#6f86a3,#9a3a2c 55%,#3b3a3a)"></div>
    <h4>Blog Tittle here</h4>
    <p>Mauris vel lacus vitae felis vestibulum volutpat Etiam est nunc venenatis in tristique</p>
    <a>READ MORE</a>
  </div>
  <div class="more-blogs">VIEW MORE BLOGS</div>
</section>

<section class="abs panel feed">
  <div class="feed-head">Chatter Feed<div class="follow-chip"></div></div>
  <div class="feed-item" style="top:78px">
    <div class="avatar" role="img" aria-label="Profile photo"></div>
    <h4>Vestibulum ligula <span>@ inceptos hymenaeos</span></h4>
    <p>Curabitur metus ipsum luctus eu malesuada ut tincidunt sed diam Donec quis mi sed magna hendrerit accumsan</p>
    <time style="top:64px">2 days ago</time>
  </div>
  <div class="feed-item" style="top:182px">
    <div class="avatar" role="img" aria-label="Profile photo"></div>
    <h4>Praesent sit amet <span>@ inceptos hymenaeos</span></h4>
    <p>Curabitur metus ipsum luctus eu malesuada ut tincidunt sed diam Donec quis mi sed magna hendrerit accumsan porttitor mattis enim In massa libero interdum nec dictum vel blandit sed nulla In ullamcorper est eget temp</p>
    <time style="top:100px">2 days ago</time>
  </div>
  <div class="scroll-track"></div><div class="scroll-thumb"></div>
</section>

<!-- footer -->
<footer class="abs footer">
  <div class="footer-col" style="left:135px"><h5>COMPANY</h5><ul><li>Trucks for Sale</li><li>Truck Resources</li><li>New Truck Models</li><li>Check Truck Prices</li></ul></div>
  <div class="divider" style="left:297px"></div>
  <div class="footer-col" style="left:342px"><h5>SELL TRUCK</h5><ul><li>Private Truck Sellers</li><li>Truck Dealers</li><li>Commercial Truck</li><li>View More</li></ul></div>
  <div class="divider" style="left:505px"></div>
  <div class="footer-col" style="left:549px"><h5>RESOURCES</h5><ul><li>Blogs &amp; News</li><li>Our Support</li><li>Register Now</li><li>Find a Dealer</li></ul></div>
  <div class="divider" style="left:693px"></div>
  <div class="footer-col" style="left:739px"><h5>FOLLOW US</h5><p>Please connect with us on</p><div class="follow-circles"><span></span><span></span><span></span><span></span></div></div>
</footer>
<div class="abs footer-base">© 2016 Company Name &nbsp;All right reserved &nbsp;Term of Use</div>

</body>
</html>
```